Brightfern Systems Business Cards

We need a new business card design for an Electrical company that also focuses on Audio Visual and Communications. We would like to see designs using our new company logo attached. The cards are for two different people outlined below. Full contact details will be provided when design winner is awarded, use generic information for now. Business card is to be double sided and we are open to layout and design ideas.

Target Market(s)

Residential & Commercial

Industry/Entity Type

Electrical

Contact Information for Business Card

Name: Corwin Bell - Senior Electrician, Name: Milo Grant - Technology Specialist.

Font styles to use
Sans Serif

Colors
0555a3
ffffff
000000

Requirements
Must have
• mobile number, email address, website address, PO Box address,
• A main heading somewhere on the card stating ELECTRICAL SERVICES - AUDIO VISUAL SALES & INSTALLATION - COMMUNICATIONS

```html
<!DOCTYPE html>
<html lang="en">
<head>
<meta charset="utf-8">
<title>Brightfern Systems – Business Card</title>
<link href="https://fonts.googleapis.com/css2?family=Source+Sans+3:wght@400;600&display=swap" rel="stylesheet">
<style>
  :root {
    --page-bg: #e9e6e2;
    --card-deep: #152a5c;
    --card-mid: #1f3a78;
    --card-edge: #172c62;
    --name-blue: #63a7dd;
    --text-light: #d9dde6;
    --icon-light: #b9c2d4;
    --brand-silver: #c9c6c0;
  }
  * { margin: 0; padding: 0; box-sizing: border-box; }
  html, body {
    width: 1200px;
    height: 970px;
    overflow: hidden;
    background: var(--page-bg);
    font-family: "Source Sans 3", "Source Sans Pro", Arial, sans-serif;
  }
  .card {
    position: absolute;
    left: 150px;
    top: 235px;
    width: 900px;
    height: 500px;
    border-radius: 4px;
    background: linear-gradient(135deg, var(--card-deep) 0%, var(--card-mid) 55%, var(--card-edge) 100%);
    box-shadow: 0 6px 24px rgba(0, 0, 0, 0.18);
    color: var(--text-light);
  }
  .holder-name {
    position: absolute;
    left: 35px;
    top: 30px;
    font-size: 31px;
    font-weight: 600;
    color: var(--name-blue);
    letter-spacing: 0.2px;
  }
  .holder-role {
    position: absolute;
    left: 35px;
    top: 76px;
    font-size: 19px;
    font-weight: 400;
  }
  .address {
    position: absolute;
    left: 35px;
    top: 280px;
    font-size: 21px;
    line-height: 32px;
  }
  .contact-list {
    position: absolute;
    left: 35px;
    top: 372px;
    list-style: none;
  }
  .contact-item {
    display: flex;
    align-items: center;
    height: 32px;
    font-size: 21px;
  }
  .contact-icon {
    width: 18px;
    height: 18px;
    margin-right: 24px;
    flex: none;
  }
  .brand-name {
    position: absolute;
    right: 48px;
    bottom: 38px;
    text-align: center;
    font-size: 36px;
    line-height: 40px;
    font-weight: 600;
    letter-spacing: 2px;
    color: var(--brand-silver);
  }
</style>
</head>
<body>
  <article class="card">
    <h1 class="holder-name">Corwin Bell</h1>
    <p class="holder-role">Senior Electrician</p>

    <p class="address">Your Commercial or office address<br>in just two line with pincode</p>

    <ul class="contact-list">
      <li class="contact-item">
        <svg class="contact-icon" viewBox="0 0 18 18" aria-hidden="true">
          <rect x="4.5" y="1" width="9" height="16" rx="1.5" fill="none" stroke="var(--icon-light)" stroke-width="1.6"/>
          <circle cx="9" cy="14" r="1" fill="var(--icon-light)"/>
        </svg>
        <span>00.00.00.0000</span>
      </li>
      <li class="contact-item">
        <svg class="contact-icon" viewBox="0 0 18 18" aria-hidden="true">
          <rect x="1.5" y="4" width="15" height="10" fill="var(--icon-light)"/>
          <path d="M1.5 4 L9 10 L16.5 4" fill="none" stroke="var(--card-deep)" stroke-width="1.3"/>
        </svg>
        <span>yourname@yourwebsite.com</span>
      </li>
      <li class="contact-item">
        <svg class="contact-icon" viewBox="0 0 18 18" aria-hidden="true">
          <circle cx="9" cy="9" r="6.5" fill="none" stroke="var(--icon-light)" stroke-width="1.4"/>
          <ellipse cx="9" cy="9" rx="2.8" ry="6.5" fill="none" stroke="var(--icon-light)" stroke-width="1.1"/>
          <line x1="2.5" y1="9" x2="15.5" y2="9" stroke="var(--icon-light)" stroke-width="1.1"/>
        </svg>
        <span>www.yourwebsite.com</span>
      </li>
    </ul>

    <p class="brand-name">BRIGHTFERN<br>SYSTEMS</p>
  </article>
</body>
</html>
```